Professional Home Buyer business card needed

I need a pretty straight forward business card designed. We help people that NEED to sell their homes solve problems. We perform all types of Real Estate transactions including flip, wholesale, investment, rental property and multi family. The card will mainly be used to give to prospective Sellers but will also be given to Real Estate Investors as well. It should professional and very easy to read, most clients are older people.

Target Market(s)

Distressed home sellers as well as Real Estate investors

Industry/Entity Type

Real Estate

Contact Information for Business Card

should be a professional layout

Colors
ec1f27
ffffff
000000

Requirements
Must have
• Large logo on back and smaller one on front. should utilize Red, white, and black.
• I am thinking of using a soft touch coating on the card so keep that in mind.
• Contact info should be very easy to read, think older clients.
Nice to have
• I would like to see a design with rounded corners on the card
Should not have
• pictures of homes or other home graphics.

```html
<!DOCTYPE html>
<html lang="en">
<head>
<meta charset="utf-8">
<title>Summit Home Buyers – Business Card</title>
<link href="https://fonts.googleapis.com/css2?family=Open+Sans:wght@400;600;800&display=swap" rel="stylesheet">
<style>
  :root {
    --red: #ec1f27;
    --white: #ffffff;
    --black: #000000;
    --ink: #222222;
    --grey: #6b6b6b;
    --divider: #c9c9c9;
    --backdrop: #2a2a2a;
  }
  * { margin: 0; padding: 0; box-sizing: border-box; }
  html, body {
    width: 1200px; height: 892px; overflow: hidden;
    background: var(--backdrop);
    font-family: "Open Sans", Arial, sans-serif;
  }
  .stage {
    width: 1200px; height: 892px;
    display: flex; flex-direction: column; align-items: center; justify-content: center; gap: 40px;
  }
  .card {
    width: 700px; height: 400px; border-radius: 16px; overflow: hidden; position: relative;
    box-shadow: 0 10px 30px rgba(0,0,0,.5);
  }
  /* Back */
  .card-back { background: var(--black); display: flex; flex-direction: column; align-items: center; justify-content: center; }
  .tagline {
    color: var(--white); font-size: 13px; font-weight: 600; letter-spacing: 6px; text-transform: uppercase;
    margin-bottom: 18px;
  }
  .brand-back {
    color: var(--white); font-weight: 800; font-size: 64px; letter-spacing: 2px; line-height: 1;
    display: flex; align-items: center; gap: 18px;
  }
  .brand-mark { width: 22px; height: 22px; background: var(--red); }
  .brand-sub {
    color: var(--white); font-weight: 800; font-size: 24px; letter-spacing: 12px; margin-top: 16px; text-transform: uppercase;
  }
  /* Front */
  .card-front { background: var(--white); }
  .front-band {
    height: 178px; background: var(--black);
    display: flex; align-items: center; justify-content: center;
  }
  .brand-front { color: var(--white); font-weight: 800; font-size: 46px; letter-spacing: 2px; display: flex; align-items: center; gap: 14px; }
  .brand-front .brand-mark { width: 16px; height: 16px; }
  .front-body { display: flex; padding: 34px 40px 0 40px; height: 190px; }
  .person { flex: 1; text-align: right; padding-right: 26px; }
  .person-name { color: var(--red); font-weight: 800; font-size: 24px; line-height: 1.1; }
  .person-title { color: var(--ink); font-size: 16px; font-weight: 600; text-transform: uppercase; margin-bottom: 14px; }
  .person-address { color: var(--grey); font-size: 17px; line-height: 1.35; }
  .divider { width: 1px; background: var(--divider); height: 110px; }
  .contacts { flex: 1; padding-left: 26px; list-style: none; }
  .contacts li { display: flex; align-items: center; gap: 12px; color: var(--grey); font-size: 17px; line-height: 1.6; white-space: nowrap; }
  .contacts svg { width: 16px; height: 16px; fill: var(--red); flex: none; }
  .front-strip { position: absolute; left: 0; right: 0; bottom: 0; height: 32px; background: var(--red); }
</style>
</head>
<body>
<main class="stage">
  <section class="card card-back" aria-label="Card back">
    <p class="tagline">We make selling simple!</p>
    <div class="brand-back"><span class="brand-mark"></span>SUMMIT</div>
    <p class="brand-sub">Home Buyers</p>
  </section>

  <section class="card card-front" aria-label="Card front">
    <div class="front-band">
      <div class="brand-front"><span class="brand-mark"></span>SUMMIT</div>
    </div>
    <div class="front-body">
      <div class="person">
        <p class="person-name">MARK ELLISON</p>
        <p class="person-title">President</p>
        <p class="person-address">1270 Carroway Lane<br>Elm Ridge, NY 10099</p>
      </div>
      <div class="divider"></div>
      <ul class="contacts">
        <li><svg viewBox="0 0 16 16"><path d="M3 1h3l1 4-2 1c1 2 3 4 5 5l1-2 4 1v3c0 1-1 2-2 2C7 15 1 9 1 3c0-1 1-2 2-2z"/></svg>555 0142 7781</li>
        <li><svg viewBox="0 0 16 16"><path d="M4 0h8a1 1 0 0 1 1 1v14a1 1 0 0 1-1 1H4a1 1 0 0 1-1-1V1a1 1 0 0 1 1-1zm1 2v10h6V2zm3 11a1 1 0 1 0 0 2 1 1 0 0 0 0-2z"/></svg>555 0198 4026</li>
        <li><svg viewBox="0 0 16 16"><path d="M1 3h14v10H1zm1 1v1l6 4 6-4V4z"/></svg>mark@summithomebuyer.com</li>
        <li><svg viewBox="0 0 16 16"><circle cx="8" cy="8" r="7"/></svg>www.summithomebuyer.com</li>
      </ul>
    </div>
    <div class="front-strip"></div>
  </section>
</main>
</body>
</html>
```